Conference for Teenagers Needs Event Graphics

I am in need of event graphics for our upcoming event. This event, titled "Kestrel Youth Rally", is a weekend event for teenagers 11-19 years old. They hear from speakers, listen to a band, and do other fun activities. Our theme is "Together." Graphic design should have a young adult/older teen feel. Clean, not very bright colors.

Event Info:
November 6-8, 2020
Pellworth Exhibit Hall, Sioux Falls, SD
Speakers: TBD (will give name and picture before final approval)
Worship: (band name TBD before final approval)
KestrelYouthRally.com
#417KR
Our Organization Logo (attached): Lumen Forward

Once designed, I need the following graphics file sizes:
-11x17 Vertical Poster design: include all event info AND a "blank" spot/box for groups to add their own details/information. Also include the QRV logo and our organization logo Lumen Forward in someway.
-4x3 horizontal postcard: include all event info on 1 side including LumenForward logo and QRV; blank backside
-Main Graphic Slide: formatted to fit a widescreen 16x9 screen. Include event name, hashtag, QRV and Lumen Forward logo
-social media graphics for event: can incorporate some or all of the event details
-4.25x 2.75 vertical badge: include event title on front with Lumen Forward logo

Target Market(s)

Young adults or older teenagers

Requirements
Must have
• -event info
-Lumen Forward Logo & QRV logo

```html
<!DOCTYPE html>
<html lang="en">
<head>
<meta charset="utf-8">
<title>Kestrel Youth Rally — Poster</title>
<link rel="stylesheet" href="https://fonts.googleapis.com/css2?family=Montserrat:wght@600;800;900&family=Roboto+Condensed:wght@700&display=swap">
<style>
  :root {
    --sky: #5cc8ea;
    --sky-deep: #2f8fc4;
    --ink: #111318;
    --navy: #1b2030;
    --red: #e0262b;
    --orange: #f39b1f;
    --white: #ffffff;
    --photo-a: #b0406a;
    --photo-b: #2a1a3a;
  }
  html, body { margin: 0; padding: 0; overflow: hidden; background: var(--white); }
  .poster {
    position: relative;
    width: 778px;
    height: 1200px;
    overflow: hidden;
    background: linear-gradient(160deg, #7fd6f2 0%, var(--sky) 45%, var(--sky-deep) 100%);
    font-family: "Montserrat", sans-serif;
  }
  .backdrop { position: absolute; inset: 0; }
  .brand {
    position: absolute;
    top: 22px;
    display: flex;
    align-items: center;
    gap: 8px;
    color: var(--white);
    font-weight: 800;
    font-size: 22px;
    letter-spacing: 0.5px;
    white-space: nowrap;
  }
  .brand-mark { width: 16px; height: 16px; background: var(--white); border-radius: 50%; }
  .brand--org { left: 20px; }
  .brand--partner { left: 250px; }
  .title-block {
    position: absolute;
    left: 190px;
    top: 140px;
    width: 470px;
    height: 300px;
    transform: rotate(-4deg);
  }
  .title-card {
    position: absolute;
    left: 20px;
    right: 10px;
    top: 40px;
    height: 200px;
    background: var(--ink);
    border-radius: 28px;
    box-shadow: 10px 12px 0 rgba(0,0,0,0.25);
  }
  .title-ribbon {
    position: absolute;
    background: var(--red);
    color: var(--white);
    font-weight: 800;
    text-align: center;
    border-radius: 10px;
    text-transform: uppercase;
    line-height: 1;
  }
  .title-ribbon--top { left: 60px; top: 14px; width: 340px; font-size: 32px; padding: 10px 0; }
  .title-ribbon--bottom { left: 150px; top: 205px; width: 290px; font-size: 34px; padding: 10px 0; }
  .title-main {
    position: absolute;
    left: 20px; right: 10px; top: 82px;
    margin: 0;
    text-align: center;
    color: var(--white);
    font-weight: 900;
    font-size: 100px;
    line-height: 1;
  }
  .date-tag {
    position: absolute;
    left: 246px;
    top: 460px;
    background: var(--orange);
    border: 3px solid var(--ink);
    color: var(--ink);
    font-family: "Roboto Condensed", sans-serif;
    font-weight: 700;
    font-size: 38px;
    padding: 2px 14px;
  }
  .venue {
    position: absolute;
    left: 246px;
    top: 520px;
    margin: 0;
    color: var(--ink);
    font-family: "Roboto Condensed", sans-serif;
    font-weight: 700;
    font-size: 32px;
    line-height: 1.2;
  }
  .hashtag {
    position: absolute;
    left: 246px;
    top: 605px;
    margin: 0;
    color: var(--white);
    font-family: "Roboto Condensed", sans-serif;
    font-weight: 700;
    font-size: 46px;
  }
  .website {
    position: absolute;
    left: 738px;
    top: 480px;
    transform-origin: left top;
    transform: rotate(90deg);
    color: var(--orange);
    font-weight: 600;
    font-size: 24px;
    white-space: nowrap;
  }
  .speakers {
    position: absolute;
    left: 60px;
    top: 1160px;
    transform-origin: left top;
    transform: rotate(-90deg);
    color: var(--white);
    font-weight: 800;
    font-size: 40px;
    white-space: nowrap;
  }
  .photo {
    position: absolute;
    left: 392px;
    top: 805px;
    width: 380px;
    height: 380px;
    border-radius: 50%;
    border: 8px solid var(--red);
    box-sizing: border-box;
    background: radial-gradient(circle at 45% 40%, var(--photo-a) 0%, #6b2a58 45%, var(--photo-b) 100%);
  }
</style>
</head>
<body>
<main class="poster">
  <svg class="backdrop" width="778" height="1200" viewBox="0 0 778 1200" aria-hidden="true">
    <polygon points="0,180 110,250 190,1200 0,1200" fill="var(--ink)"/>
    <polygon points="0,770 778,650 778,1200 0,1200" fill="var(--navy)"/>
    <polygon points="110,250 130,250 210,1200 190,1200" fill="var(--red)"/>
    <polygon points="0,760 778,640 778,650 0,770" fill="var(--red)"/>
    <polygon points="0,0 220,0 0,120" fill="var(--ink)"/>
    <polygon points="520,110 600,150 560,180" fill="var(--red)"/>
    <polygon points="150,300 200,250 195,320" fill="var(--red)"/>
    <polygon points="650,390 720,420 660,440" fill="var(--red)"/>
  </svg>

  <div class="brand brand--org"><span class="brand-mark"></span>Lumen Forward</div>
  <div class="brand brand--partner">QRV</div>

  <header class="title-block">
    <div class="title-card"></div>
    <div class="title-ribbon title-ribbon--top">Kestrel</div>
    <h1 class="title-main">YOUTH</h1>
    <div class="title-ribbon title-ribbon--bottom">Rally</div>
  </header>

  <div class="date-tag">6-8 NOVEMBER</div>
  <p class="venue">Pellworth Exhibit Hall,<br>Sioux Falls, SD</p>
  <p class="hashtag">#417KR</p>

  <div class="website">KestrelYouthRally.com</div>
  <div class="speakers">Speakers: TBD</div>

  <div class="photo" role="img" aria-label="Photo of a group of smiling teenagers singing together into a microphone"></div>
</main>
</body>
</html>
```